TRAW - Stewardship Website

We need a web design for our stewardship ministry. You can see what we have now: http://projects.tolrawq.org/

We need a new design and a total change of the website.

Ministry

```html
<!DOCTYPE html>
<html lang="en">
<head>
<meta charset="utf-8">
<title>TRAW Kingdom Stewards Projects</title>
<link href="https://fonts.googleapis.com/css2?family=PT+Sans:ital,wght@0,400;0,700;1,400;1,700&family=PT+Sans+Narrow:wght@400;700&family=Open+Sans:wght@400;600;700;800&display=swap" rel="stylesheet">
<style>
:root{
  --page:#ffffff;
  --head-bg:#eef1f5;
  --green-top:#8fd33a;
  --green-mid:#6cb120;
  --green-dark:#4f8c12;
  --blue-dark:#0b3f79;
  --blue:#0f5aa6;
  --blue-mid:#1466b8;
  --sky:#bcdcf3;
  --text:#333;
  --heading-green:#4e8d13;
  --heading-blue:#0d4f92;
}
*{margin:0;padding:0;box-sizing:border-box}
html,body{width:1200px;height:1087px;overflow:hidden;background:var(--page)}
body{font-family:"PT Sans",sans-serif;color:var(--text)}
.canvas{position:relative;width:1200px;height:1087px;overflow:hidden;background:var(--page)}
.abs{position:absolute}

/* header */
.header{left:0;top:0;width:1200px;height:130px;background:var(--head-bg)}
.brand{left:166px;top:24px;display:flex;align-items:center;gap:12px}
.brand-mark{width:80px;height:80px;border-radius:50%;background:var(--blue);border:5px solid var(--green-mid)}
.brand-name{font-family:"PT Sans",sans-serif;font-weight:700;font-size:30px;color:var(--heading-blue)}
.tagline{left:474px;top:68px;font-style:italic;font-weight:700;font-size:20px;color:#222}
.contact{left:763px;top:16px;font-size:15px;line-height:21px;color:#111}
.contact b{color:var(--heading-green)}
.contact svg{vertical-align:-3px;margin-right:6px}
.search-label{left:764px;top:76px;font-size:14px;color:var(--heading-blue);letter-spacing:.3px}
.search{left:822px;top:67px;width:216px;height:32px;border-radius:16px;background:#fff;border:1px solid #c9d2dc;box-shadow:inset 0 1px 3px rgba(0,0,0,.15)}
.search-placeholder{left:38px;top:8px;font-size:11px;color:#888}
.search-icon{left:14px;top:9px}
.search-go{right:3px;top:3px;width:25px;height:25px;border-radius:50%;background:var(--blue);color:#fff;font-size:9px;font-weight:700;text-align:center;line-height:25px}

/* nav */
.nav-band{left:0;top:130px;width:1200px;height:92px;background:linear-gradient(var(--green-top),var(--green-mid) 55%,var(--green-dark))}
.blue-strip{left:0;top:222px;width:1200px;height:30px;background:var(--blue-dark)}
.nav{left:0;top:130px;width:1200px;height:66px}
.nav-item{position:absolute;top:21px;font-family:"PT Sans Narrow",sans-serif;font-weight:700;font-size:20px;color:#fff;text-transform:uppercase;transform:translateX(-50%);white-space:nowrap}
.nav-active{left:520px;top:120px;width:144px;height:76px;background:linear-gradient(var(--blue-mid),var(--blue-dark));border-top:8px solid var(--green-top)}
.nav-active span{display:block;text-align:center;margin-top:23px;font-family:"PT Sans Narrow",sans-serif;font-weight:700;font-size:20px;color:#fff;white-space:nowrap}
.dropdown{left:520px;top:196px;width:188px;height:198px;background:var(--blue-dark);padding-top:9px;z-index:5}
.dropdown li{list-style:none;height:22.6px;line-height:22px;padding-left:16px;font-size:11.5px;color:#fff;border-bottom:1px solid #2a67a8;text-transform:uppercase}
.dropdown li.current{background:#062c57}

/* hero */
.hero-frame{left:144px;top:196px;width:912px;height:368px;background:var(--sky);border-radius:12px}
.hero-photo{left:166px;top:220px;width:868px;height:332px;border:3px solid #fff;border-radius:14px;background:linear-gradient(120deg,#3b2a20 0%,#2a67b8 35%,#b9a98c 60%,#e1d7c3 80%,#6a4e36 100%)}
.banner{left:234px;top:552px;width:734px;height:58px;background:linear-gradient(var(--blue),var(--blue-dark));clip-path:polygon(0 0,100% 0,99% 100%,1% 100%);color:#fff;font-family:"Open Sans",sans-serif;font-weight:800;font-size:28px;text-align:center;line-height:60px;letter-spacing:-.3px}

/* welcome */
.welcome{left:166px;top:630px;width:366px}
.welcome-kicker{font-size:14px;color:var(--heading-blue);line-height:15px}
.welcome-title{font-size:18px;color:var(--heading-green);line-height:20px}
.welcome-title small{font-size:13px;color:var(--heading-blue)}
.rule{height:6px;margin-top:6px;background:repeating-linear-gradient(90deg,#999 0 1px,transparent 1px 3px)}
.welcome-photo{left:166px;top:689px;width:122px;height:123px;border-radius:8px;background:linear-gradient(160deg,#b9b3ad,#4e433d 60%,#6f5d50)}
.body-copy{font-family:Tahoma,"PT Sans",sans-serif;font-size:11.6px;line-height:14px;text-align:justify;color:#333}
.copy-side{left:302px;top:690px;width:230px}
.copy-side p+p{margin-top:5px}
.copy-full{left:166px;top:823px;width:366px}
.copy-last{left:166px;top:934px;width:366px}

/* side panels */
.panel{background:var(--sky);clip-path:polygon(0 0,100% 0,96% 100%,4% 100%)}
.panel-news{left:542px;top:625px;width:242px;height:350px;border-radius:10px}
.panel-projects{left:794px;top:625px;width:242px;height:258px;border-radius:10px}
.panel-head{height:42px;background:linear-gradient(var(--green-top),var(--green-dark));border-radius:8px 8px 0 0;color:#fff;font-size:17px;line-height:44px;padding-left:20px;text-transform:uppercase}
.news-card{left:560px;top:642px;width:206px;height:326px}
.projects-card{left:812px;top:642px;width:206px;height:232px}
.panel-body{background:#fff;padding:14px 0 0 12px;height:calc(100% - 42px)}
.bullets li{list-style:none;position:relative;padding-left:18px;font-size:11.5px;line-height:13.5px;color:#333;margin-bottom:4px}
.bullets li::before{content:"";position:absolute;left:3px;top:4px;width:6px;height:6px;border-radius:50%;background:var(--blue-dark)}
.projects-card .bullets li{font-size:12px;line-height:14px;margin-bottom:8.6px}
.more-link{font-size:11.5px;color:var(--heading-blue);text-decoration:underline;margin:6px 0 0 4px;display:block}
.resources{left:815px;top:886px;width:201px;height:80px;border-radius:8px;background:linear-gradient(var(--blue-mid),var(--blue-dark));color:#fff;padding:8px 20px}
.resources h3{font-size:16px;font-weight:700;line-height:18px}
.resources li{list-style:none;font-size:12px;font-weight:700;line-height:17px}

/* footer */
.footer-line{left:0;top:985px;width:1200px;height:4px;background:var(--green-mid)}
.footer{left:0;top:989px;width:1200px;height:98px;background:var(--head-bg);text-align:center}
.follow{margin-top:24px;font-size:15px;color:#111}
.follow i{display:inline-block;width:16px;height:16px;border-radius:3px;vertical-align:-3px;margin-left:4px}
.follow .s1{background:#3b5998}.follow .s2{background:#4ab3e8}
.footer-links{margin-top:6px;font-size:11px;color:#333;line-height:14px}
</style>
</head>
<body>
<div class="canvas">

  <header class="abs header">
    <div class="abs brand">
      <span class="brand-mark"></span>
      <span class="brand-name">Tolrawq</span>
    </div>
    <div class="abs tagline">Sharing in the Lord's Vineyard.</div>
    <div class="abs contact">
      <div><svg width="15" height="14" viewBox="0 0 15 14"><path d="M3 1h3l1 3-2 1a8 8 0 0 0 4 4l1-2 3 1v3a2 2 0 0 1-2 2A11 11 0 0 1 1 3a2 2 0 0 1 2-2z" fill="#1a5fa8"/></svg><b>Call us at:</b>&nbsp; 08031470258 &nbsp;|&nbsp; 08052369814</div>
      <div><svg width="15" height="11" viewBox="0 0 15 11"><rect x=".5" y=".5" width="14" height="10" fill="#fff" stroke="#1a5fa8"/><path d="M.5.5l7 6 7-6" fill="none" stroke="#1a5fa8"/></svg><b>Email:</b>&nbsp; projects@tolrawq.org</div>
    </div>
    <div class="abs search-label">SEARCH</div>
    <div class="abs search">
      <svg class="abs search-icon" width="13" height="13" viewBox="0 0 13 13"><circle cx="5" cy="5" r="4" fill="none" stroke="#888" stroke-width="1.5"/><path d="M8 8l4 4" stroke="#888" stroke-width="1.5"/></svg>
      <span class="abs search-placeholder">enter your text here</span>
      <span class="abs search-go">GO</span>
    </div>
  </header>

  <div class="abs nav-band"></div>
  <div class="abs blue-strip"></div>

  <div class="abs hero-frame"></div>
  <div class="abs hero-photo" role="img" aria-label="Photo of children in blue shirts playing chess at a table"></div>

  <nav class="abs nav">
    <span class="nav-item" style="left:352px">Home</span>
    <span class="nav-item" style="left:456px">About Us</span>
    <span class="nav-item" style="left:730px">Partners</span>
    <span class="nav-item" style="left:858px">Contact Us</span>
  </nav>
  <div class="abs nav-active"><span>OUR PROJECTS</span></div>
  <ul class="abs dropdown">
    <li>Support Scheme</li>
    <li>Kid &amp; Teen</li>
    <li class="current">Resource Development</li>
    <li>Green Habitat</li>
    <li>Community Integration</li>
    <li>Prison to Praise</li>
    <li>Education for All</li>
    <li>The Champion</li>
  </ul>

  <div class="abs banner">DEDICATED TO ENRICHING THE LIVES OF OTHERS.</div>

  <section class="abs welcome">
    <div class="welcome-kicker">WELCOME TO</div>
    <div class="welcome-title">TRAW'S KINGDOM STEWARDS <small>PROJECTS WEBSITE.</small></div>
    <div class="rule"></div>
  </section>
  <div class="abs welcome-photo" role="img" aria-label="Photo of a smiling child carrying a ball on the head"></div>
  <div class="abs body-copy copy-side">
    <p>Jesus instructed us in Matthew 6:33 to first aim at and strive after the kingdom and righteousness of God, in doing this the benefits of life will be available to us. To seek the kingdom, implies that we endeavour to belong to it and promote the interests of it.</p>
    <p>The major concern of the kingdom is the care and comfort of the people. King Solomon asked for wisdom to bring justice to the great</p>
  </div>
  <p class="abs body-copy copy-full">people of God, the request was granted and other enablers were added for the fulfillment of that interest. The Samaritan who helped the man that fell among thieves on his way from Jerusalem to Jericho exhibited true kingdom compassion and was justified as a good neighbour. Dorcas is another example of a heart set on kingdom interest, a heart adorned with the milk of kindness, she was known and celebrated for her good works and alms deeds. Acts 9:36.</p>
  <p class="abs body-copy copy-last">In Tolrawq International Fellowship, we are delighted to fulfill this work of compassion by providing shelter, care, food etc to the needy.</p>

  <div class="abs panel panel-news"></div>
  <section class="abs news-card">
    <div class="panel-head">Latest Project News</div>
    <div class="panel-body">
      <ul class="bullets">
        <li>Lorem ipsum dolor sit amet consectetur adipiscing elit.</li>
        <li>Vivamus dolor velit, sollicitudin porta elementum non,</li>
        <li>Sagittis vel urnauspendisse ut</li>
        <li>Urna in nisi iaculis mattis a vel</li>
        <li>Morbi interdum mi id tellus orn are dapibus.</li>
        <li>Aenean vitae ligula eu justo varius lobortis.</li>
        <li>Aenean purus sem, semper sit amet lobortis et,</li>
        <li>Dapibus non diam.</li>
        <li>Proin vel eleifend erat.</li>
        <li>Nullam erat tortor,</li>
      </ul>
      <a class="more-link">Click here for more news</a>
    </div>
  </section>

  <div class="abs panel panel-projects"></div>
  <section class="abs projects-card">
    <div class="panel-head">Our Projects</div>
    <div class="panel-body">
      <ul class="bullets">
        <li>Support Scheme</li>
        <li>Kid &amp; Teen</li>
        <li>Resource Development</li>
        <li>Green Habitat</li>
        <li>Community Integration</li>
        <li>Prison to Praise</li>
        <li>Education for All</li>
        <li>The Champion</li>
      </ul>
    </div>
  </section>

  <section class="abs resources">
    <h3>RESOURCES:</h3>
    <ul>
      <li>TRAW MAIN WEBSITE</li>
      <li>CHURCH IN THE HOUSE</li>
      <li>TRAW BUSINESS HUB</li>
    </ul>
  </section>

  <div class="abs footer-line"></div>
  <footer class="abs footer">
    <div class="follow">Follow us on: <i class="s1"></i><i class="s2"></i></div>
    <div class="footer-links">Home &nbsp;--&nbsp; About Us &nbsp;--&nbsp; Our Projects &nbsp;--&nbsp; Partners &nbsp;--&nbsp; Contact Us<br>Tolrawq International Fellowship © 2012 | Privacy Statement | Terms of Use</div>
  </footer>

</div>
</body>
</html>
```